Professional/modern business card design for construction company

We need a new business card design, double sided keeping it modern, sleek, professional and simple. We are an earthmoving business but do not want any pictures of machinery. I would like one side to have the logo and the other to have all the information, keeping with the colors in our logo. The business card will need to be able to be customised so we can use it for several different managers., we would also like to be able to use the design to apply it to other stationary ie. letterheads, notebooks etc. We do not really have a tag line but we could put on there that we specialise in - Agriculture, Civil Construction and Mining.

Contact Information for Business Card

Brolga Ridge Excavations Pty Ltd
ABN 58 402 937 615
82 Gumleaf Creek Road, Moree NSW 2400

Harold Benton
Managing Director
P 0418 639 204
E haroldbenton@brolgaridgeexc.com.au

Font styles to use
Serif
Sans Serif

Requirements
Nice to have
• I have attached some examples of ideas.
Should not have
• images of machinery

```html
<!DOCTYPE html>
<html lang="en">
<head>
<meta charset="utf-8">
<title>Brolga Ridge Excavations – Business Card</title>
<link rel="stylesheet" href="https://fonts.googleapis.com/css2?family=Montserrat:wght@500;600;700&family=Poppins:wght@400;500&display=swap">
<style>
  :root {
    --orange: #f7861f;
    --charcoal: #3d3d3d;
    --grey: #555555;
    --rule: #8a8a8a;
    --paper: #ffffff;
    --backdrop: #e9e9ea;
  }
  * { box-sizing: border-box; margin: 0; padding: 0; }
  html, body { width: 1200px; height: 874px; overflow: hidden; }
  body {
    background: var(--backdrop);
    position: relative;
    font-family: "Poppins", sans-serif;
  }
  .card {
    position: absolute;
    left: 270px;
    width: 660px;
    height: 377px;
    box-shadow: 0 6px 18px rgba(0,0,0,0.18);
  }
  .card--back {
    top: 40px;
    background: var(--orange);
    display: flex;
    align-items: center;
    justify-content: center;
  }
  .tagline {
    color: var(--paper);
    font-family: "Montserrat", sans-serif;
    font-weight: 600;
    font-size: 19px;
    line-height: 1.4;
    text-align: center;
  }
  .card--front {
    top: 437px;
    background: var(--paper);
  }
  .company-name {
    position: absolute;
    right: 52px;
    top: 48px;
    text-align: right;
    font-family: "Montserrat", sans-serif;
    font-weight: 700;
    color: var(--charcoal);
    font-size: 30px;
    line-height: 1.1;
    text-transform: uppercase;
    letter-spacing: 0.5px;
  }
  .company-name span { display: block; font-size: 16px; letter-spacing: 1.2px; }
  .person {
    position: absolute;
    left: 44px;
    top: 158px;
    width: 330px;
  }
  .person__name {
    font-family: "Montserrat", sans-serif;
    font-weight: 700;
    font-size: 25px;
    color: var(--orange);
    text-transform: uppercase;
    line-height: 1.1;
  }
  .person__role {
    font-size: 15px;
    color: var(--grey);
    padding-bottom: 10px;
    border-bottom: 1.5px solid var(--rule);
    margin-bottom: 12px;
  }
  .contact-list { list-style: none; }
  .contact-list li {
    display: flex;
    align-items: center;
    gap: 10px;
    font-size: 14px;
    color: var(--grey);
    line-height: 1.55;
    white-space: nowrap;
  }
  .contact-list svg { width: 13px; height: 13px; flex: none; fill: var(--orange); }
  .address {
    position: absolute;
    right: 52px;
    bottom: 36px;
    width: 210px;
    border-top: 1.5px solid var(--rule);
    padding-top: 12px;
    text-align: right;
    font-size: 14px;
    line-height: 1.45;
    color: var(--grey);
  }
</style>
</head>
<body>
  <section class="card card--back">
    <p class="tagline">We specialise in<br>Agriculture, Civil Construction &amp; Mining.</p>
  </section>

  <section class="card card--front">
    <div class="company-name">Brolga Ridge<span>Excavations Pty Ltd</span></div>

    <div class="person">
      <h1 class="person__name">Harold Benton</h1>
      <p class="person__role">Managing Director</p>
      <ul class="contact-list">
        <li>
          <svg viewBox="0 0 24 24" aria-hidden="true"><path d="M6.6 10.8a15.1 15.1 0 0 0 6.6 6.6l2.2-2.2c.3-.3.7-.4 1-.2 1.1.4 2.3.6 3.6.6.6 0 1 .4 1 1V20c0 .6-.4 1-1 1A17 17 0 0 1 3 4c0-.6.4-1 1-1h3.5c.6 0 1 .4 1 1 0 1.3.2 2.5.6 3.6.1.3 0 .7-.2 1z"/></svg>
          0418 639 204
        </li>
        <li>
          <svg viewBox="0 0 24 24" aria-hidden="true"><path d="M2 5h20v14H2z M2 5l10 7 10-7" fill="none" stroke="#f7861f" stroke-width="2.4"/></svg>
          haroldbenton@brolgaridgeexc.com.au
        </li>
        <li>
          <svg viewBox="0 0 24 24" aria-hidden="true"><circle cx="12" cy="12" r="10"/><path d="M2 12h20M12 2c3 3 3 17 0 20M12 2c-3 3-3 17 0 20" fill="none" stroke="#fff" stroke-width="1.5"/></svg>
          www.brolgaridgeexc.com.au
        </li>
      </ul>
    </div>

    <address class="address" style="font-style:normal">
      82 Gumleaf Creek Road<br>
      Moree NSW 2400<br>
      ABN 58 402 937 615
    </address>
  </section>
</body>
</html>
```